Wesbite design for Investment Firm

We want a basic (clean) website that follows the form, fonts and colors of our attachments. This is for a financial investment management firm, but we have a boutique (anti-Wall Street) approach. Site should have an Home Page (Logo up top - room for basic copy on bottom, Philosophy Page (room for Quarterly Letter attachment and basic copy, Performance Page (room for Performance Overview and Performance Analysis and basic copy), Team Page, Commentary Page and Contact
Updates

Reason: Some designers have asked for an extension. Again, please only use image of Train Station or Train Station Logo in design.

Target Market(s)

Small and mid-size financial advisors from across the country

Industry/Entity Type

Financial

Number of Pages Required

5+ page

Font styles to use
Other font styles liked:
• Palotino Linotype

Colors
3176b5
cfdeed
ffffff

Requirements
Must have
• Please refer to existing site www.qorvenbay.com. Of note, this is too complex / cluttered. We simply want Blur, Grey and White consistent with attachments. The copy is pretty good, but will be simplified (and no quotes)
Should not have
• No images other than train station logo and / or train station image

```html
<!DOCTYPE html>
<html lang="en">
<head>
<meta charset="utf-8">
<title>Ashford Lane Investment Company</title>
<link href="https://fonts.googleapis.com/css2?family=Roboto+Condensed:wght@300;400;700&family=Open+Sans:ital,wght@0,400;0,600;1,400&display=swap" rel="stylesheet">
<style>
:root{
  --brand:#3176b5;
  --brand-dark:#2a649c;
  --brand-light:#cfdeed;
  --ink:#2b2b2b;
  --muted:#555b63;
  --rule:#e3e6ea;
  --footer:#f2f3f4;
  --white:#ffffff;
  --nav-active:#2d2d2d;
}
*{box-sizing:border-box;margin:0;padding:0}
html,body{width:1200px;height:2715px;overflow:hidden}
body{background:var(--white);font-family:"Open Sans",Arial,sans-serif;color:var(--ink);position:relative}
.wrap{position:absolute;left:0;width:1200px}
h1,h2,h3,h4,h5{font-weight:400}

/* header */
.site-header{top:0;height:138px;text-align:center}
.brand-name{font-family:"Roboto Condensed",Arial,sans-serif;font-weight:400;font-size:46px;color:var(--brand-dark);padding-top:28px;line-height:1}
.brand-tag{font-family:"Open Sans",Arial,sans-serif;font-size:15px;color:var(--muted);margin-top:12px;letter-spacing:.5px}

/* nav */
.main-nav{top:138px;height:50px;background:linear-gradient(#3f86c9,var(--brand))}
.main-nav ul{list-style:none;display:flex;margin-left:98px;height:50px}
.main-nav li{font-family:"Roboto Condensed",Arial,sans-serif;font-size:15px;color:var(--white);padding:0 24px;line-height:50px;text-transform:uppercase}
.main-nav li.active{background:var(--nav-active)}

/* hero */
.hero{top:188px;height:519px;background:linear-gradient(110deg,#3c4650 0%,#5e6a75 40%,#8a96a0 70%,#6f7a84 100%)}
.hero-title{position:absolute;left:795px;top:232px;font-family:"Roboto Condensed",Arial,sans-serif;color:var(--white);font-weight:700;line-height:1}
.hero-title .t1{font-size:40px;display:block}
.hero-title .t2{font-size:56px;display:block;margin-top:8px}
.btn-more{position:absolute;left:799px;top:360px;width:126px;height:30px;background:var(--brand-light);color:var(--brand-dark);font-family:"Roboto Condensed",Arial,sans-serif;font-size:13px;font-weight:700;text-align:center;line-height:30px;border-radius:2px}
.hero-arrow{position:absolute;top:240px}

/* about */
.about{top:707px;height:328px;text-align:center}
.section-title{font-family:"Roboto Condensed",Arial,sans-serif;font-weight:700;font-size:32px;color:var(--ink);padding-top:88px}
.about p{font-size:12.5px;line-height:22px;color:var(--muted);width:880px;margin:18px auto 0}
.about p + p{margin-top:14px}

/* services */
.services{top:1035px;height:460px}
.services svg.band{position:absolute;left:0;top:0}
.services-title{position:absolute;top:95px;width:1200px;text-align:center;font-family:"Roboto Condensed",Arial,sans-serif;font-weight:300;font-size:34px;color:var(--white)}
.services-title:after{content:"";display:block;width:62px;height:2px;background:var(--white);margin:18px auto 0}
.service{position:absolute;top:210px;width:300px;color:var(--white)}
.service .icon{position:absolute;left:0;top:0}
.service h3{margin-left:94px;font-family:"Roboto Condensed",Arial,sans-serif;font-size:21px}
.service p{margin-left:94px;font-size:11.5px;line-height:20px;margin-top:10px;opacity:.92;font-weight:600}
.service .read{margin-left:94px;margin-top:14px;font-family:"Roboto Condensed",Arial,sans-serif;font-size:12.5px;font-weight:700}

/* commentary */
.commentary{top:1540px;height:460px}
.col-title{position:absolute;font-family:"Roboto Condensed",Arial,sans-serif;font-weight:400;font-size:25px;color:var(--ink)}
.post{position:absolute;left:98px;width:676px;height:160px;border-bottom:1px solid var(--rule)}
.post .thumb{position:absolute;left:0;top:0;width:216px;height:142px}
.post h4{position:absolute;left:237px;top:0;font-family:"Roboto Condensed",Arial,sans-serif;font-size:19px}
.post .date{position:absolute;left:237px;top:34px;font-size:13px;font-style:italic;color:var(--brand);display:flex;align-items:center;gap:6px}
.post p{position:absolute;left:237px;top:62px;width:400px;font-size:11.5px;line-height:23px;color:var(--muted)}
.letter{position:absolute;left:828px;top:78px;width:272px;height:324px;background:var(--brand);padding:10px}
.letter .page{width:100%;height:100%;background:linear-gradient(#ffffff,#f4f5f6)}

/* quote */
.quote{top:2038px;height:310px;background:linear-gradient(90deg,#3574b1,#3c7fbe 50%,#3372b0);text-align:center;color:var(--white)}
.quote-mark{position:absolute;left:560px;top:40px}
.quote p{position:absolute;left:210px;top:130px;width:780px;font-size:11.5px;line-height:20px}
.quote cite{position:absolute;left:0;top:210px;width:1200px;font-style:italic;font-size:16px}
.dots{position:absolute;left:550px;top:262px;display:flex;gap:6px}
.dots span{width:28px;height:3px;background:rgba(255,255,255,.5)}
.dots span.on{background:var(--white)}

/* footer */
.site-footer{top:2348px;height:307px;background:var(--footer)}
.foot-brand{position:absolute;left:78px;top:112px;width:274px;text-align:center}
.foot-brand .name{font-family:"Roboto Condensed",Arial,sans-serif;font-weight:400;font-size:19px;color:var(--brand-dark);white-space:nowrap}
.foot-brand .tag{font-size:9.5px;color:var(--muted);margin-top:4px}
.socials{display:flex;gap:4px;justify-content:center;margin-top:18px}
.socials span{width:22px;height:22px;border:1px solid #5a5f66;border-radius:50%}
.foot-col{position:absolute;top:68px}
.foot-col h5{font-family:"Roboto Condensed",Arial,sans-serif;font-size:19px;color:var(--ink);text-transform:uppercase}
.contact-list{list-style:none;margin-top:20px}
.contact-list li{display:flex;gap:14px;font-size:12.5px;color:var(--muted);line-height:20px;margin-bottom:12px}
.contact-list li.addr{font-size:11px;line-height:20px}
.news p{font-size:11px;line-height:18px;color:var(--muted);width:260px;margin-top:14px}
.field{width:251px;height:38px;background:var(--white);border:1px solid #dcdfe3;font-size:11px;color:var(--ink);padding-left:12px;line-height:36px;margin-top:10px}
.sub-row{display:flex;margin-top:8px}
.sub-row .field{width:160px;margin-top:0}
.btn-sub{width:91px;height:38px;background:var(--brand);color:var(--white);font-family:"Roboto Condensed",Arial,sans-serif;font-size:13px;text-align:center;line-height:38px}
.links{list-style:none;margin-top:14px}
.links li{font-size:11px;color:var(--muted);line-height:22.5px}
.copyright{top:2655px;height:60px;border-top:1px solid var(--rule);text-align:center;font-size:11px;line-height:60px;color:var(--ink)}
</style>
</head>
<body>

<header class="wrap site-header">
  <div class="brand-name">Ashford Lane Investment Company</div>
  <div class="brand-tag">Boutique Portfolio Management</div>
</header>

<nav class="wrap main-nav">
  <ul>
    <li class="active">Home</li><li>Philosophy</li><li>Performance</li><li>Team</li><li>Commentary</li><li>Contact Us</li>
  </ul>
</nav>

<section class="wrap hero">
  <div role="img" aria-label="Photo of hands working on a laptop showing financial charts" style="position:absolute;inset:0"></div>
  <svg class="hero-arrow" style="left:40px" width="30" height="54" viewBox="0 0 30 54"><path d="M26 2 L4 27 L26 52" fill="none" stroke="#fff" stroke-width="2.5"/></svg>
  <svg class="hero-arrow" style="left:1140px" width="30" height="54" viewBox="0 0 30 54"><path d="M4 2 L26 27 L4 52" fill="none" stroke="#fff" stroke-width="2.5"/></svg>
  <h1 class="hero-title"><span class="t1">ASHFORD LANE</span><span class="t2">INVESTMENT</span></h1>
  <div class="btn-more">LEARN MORE &#187;</div>
</section>

<section class="wrap about">
  <h2 class="section-title">ASHFORD LANE INVESTMENT COMPANY</h2>
  <p>We founded Ashford Lane Investment Company in 1999, initially managing wealth from our family and friends in the town of Ashford Lane. The high expectations of our original investors is a key contributor to our value driven investment philosophy.</p>
  <p>Based in Dallas, TX, we manage assets for both individuals and institutions. Our investment methodology stresses absolute returns vs. relative performance, blending a combination of fundamental analysis, discipline and patience with the goal of preserving and compounding capital.</p>
</section>

<section class="wrap services">
  <svg class="band" width="1200" height="460" viewBox="0 0 1200 460">
    <polygon points="0,0 1200,0 1200,386 600,460 0,386" fill="#3a78b6"/>
  </svg>
  <h2 class="services-title">WHAT WE DO</h2>
  <div class="service" style="left:96px">
    <svg class="icon" width="80" height="80" viewBox="0 0 80 80"><circle cx="40" cy="40" r="38" fill="#fff"/><circle cx="40" cy="40" r="33" fill="none" stroke="#3176b5" stroke-width="2"/><path d="M40 40 V26 A14 14 0 1 1 26 40 Z" fill="#3176b5"/><path d="M37 37 H24 A13 13 0 0 1 37 24 Z" fill="#3176b5"/></svg>
    <h3>Performance Overview</h3>
    <p>Sed ut perspiciatis unde omnis iste natus error sit voluptatem accusatium doloremque laudantium</p>
    <div class="read">READ MORE &#10148;</div>
  </div>
  <div class="service" style="left:448px">
    <svg class="icon" width="80" height="80" viewBox="0 0 80 80"><circle cx="40" cy="40" r="38" fill="#fff"/><circle cx="40" cy="40" r="33" fill="none" stroke="#3176b5" stroke-width="2"/><path d="M26 28 V52 H54" fill="none" stroke="#3176b5" stroke-width="2.5"/><path d="M30 46 L37 38 L42 43 L52 32" fill="none" stroke="#3176b5" stroke-width="2.5"/></svg>
    <h3>Performance Analysis</h3>
    <p>Sed ut perspiciatis unde omnis iste natus error sit voluptatem accusatium doloremque laudantium</p>
    <div class="read">READ MORE &#10148;</div>
  </div>
  <div class="service" style="left:800px">
    <svg class="icon" width="80" height="80" viewBox="0 0 80 80"><circle cx="40" cy="40" r="38" fill="#fff"/><circle cx="40" cy="40" r="33" fill="none" stroke="#3176b5" stroke-width="2"/><path d="M31 26 H44 L51 33 V54 H31 Z" fill="#3176b5"/><path d="M35 40 H47 M35 45 H47 M35 50 H44" stroke="#fff" stroke-width="2"/></svg>
    <h3>Verification Statement</h3>
    <p>Sed ut perspiciatis unde omnis iste natus error sit voluptatem accusatium doloremque laudantium</p>
    <div class="read">READ MORE &#10148;</div>
  </div>
</section>

<section class="wrap commentary">
  <h2 class="col-title" style="left:98px;top:12px">LATEST COMMENTARY</h2>
  <h2 class="col-title" style="left:827px;top:16px;font-size:20px">INVESTMENT ADVISER'S LETTER</h2>
  <article class="post" style="top:78px">
    <div class="thumb" role="img" aria-label="Photo of the historic train station building" style="background:linear-gradient(135deg,#c9c6bf,#8b8578 60%,#5e594f)"></div>
    <h4>Core Equity Portfolio – Q2 2017</h4>
    <div class="date"><svg width="12" height="12" viewBox="0 0 12 12"><rect x="1" y="2" width="10" height="9" fill="#3176b5"/><rect x="2.5" y="5" width="7" height="4.5" fill="#fff"/></svg>JAN 15, 2017</div>
    <p>Based on our estimate of fair value relative to the company's current stock price, we determine each company's current margin of safety in the Core Equity quae ab illo inventore veritatis et quasi</p>
  </article>
  <article class="post" style="top:260px">
    <div class="thumb" role="img" aria-label="Photo of a small house model beside a jar of coins with a plant" style="background:linear-gradient(135deg,#6f9a3f,#3f6a2a 55%,#2c3a22)"></div>
    <h4>Sed ut perspiciatis unde omnis iste natus</h4>
    <div class="date"><svg width="12" height="12" viewBox="0 0 12 12"><rect x="1" y="2" width="10" height="9" fill="#3176b5"/><rect x="2.5" y="5" width="7" height="4.5" fill="#fff"/></svg>JAN 15, 2017</div>
    <p>Based on our estimate of fair value relative to the company's current stock price, we determine each company's current margin of safety in the Core Equity quae ab illo inventore veritatis et quasi</p>
  </article>
  <div class="letter"><div class="page" role="img" aria-label="Cover of the quarterly investment adviser's letter with a sketch of the train station"></div></div>
</section>

<section class="wrap quote">
  <svg class="quote-mark" width="80" height="70" viewBox="0 0 80 70"><path d="M4 4 H32 V32 C32 50 24 62 8 66 L6 58 C16 54 20 46 20 38 H4 Z M46 4 H74 V32 C74 50 66 62 50 66 L48 58 C58 54 62 46 62 38 H46 Z" fill="#fff"/></svg>
  <p>"An investment operation is one which, upon thorough analysis, promises safety of principal and an adequate return. Operations not meeting these requirements are speculative. Inventore veritatis et quasi architecto beatae vitae dicta sunt explicabo. Nemo enim ipsam voluptatem quia voluptas sit aspernatur aut odit aut fugit, sed quia consequuntur magni dolores eos qui ratione voluptatem sequi nesciunt.</p>
  <cite>- Harold Whitcombe, The Patient Investor</cite>
  <div class="dots"><span class="on"></span><span></span><span></span></div>
</section>

<footer class="wrap site-footer">
  <div class="foot-brand">
    <div class="name">Ashford Lane Investment Company</div>
    <div class="tag">Boutique Portfolio Management</div>
    <div class="socials"><span></span><span></span><span></span><span></span></div>
  </div>
  <div class="foot-col" style="left:390px">
    <h5>Contact Us</h5>
    <ul class="contact-list">
      <li class="addr"><svg width="14" height="18" viewBox="0 0 14 18"><path d="M7 1 C3.5 1 1 3.6 1 7 C1 11 7 17 7 17 C7 17 13 11 13 7 C13 3.6 10.5 1 7 1 Z" fill="#7a9cc4"/><circle cx="7" cy="7" r="2.2" fill="#fff"/></svg><span>2150 Maple Crest Avenue,<br>Suite 610 Dallas, TX 75201</span></li>
      <li><svg width="14" height="14" viewBox="0 0 14 14"><path d="M3 1 L5.5 4 L4 6 C5 8 6 9 8 10 L10 8.5 L13 11 L11.5 13 C6 12.5 1.5 8 1 2.5 Z" fill="#7a9cc4"/></svg><span>Phone: 214.555.0186</span></li>
      <li><svg width="14" height="14" viewBox="0 0 14 14"><rect x="1" y="3" width="12" height="8" fill="#7a9cc4"/><path d="M1 3 L7 8 L13 3" fill="none" stroke="#fff" stroke-width="1.2"/></svg><span>Email: info@qorvenbay.com</span></li>
    </ul>
  </div>
  <div class="foot-col news" style="left:657px">
    <h5>Sign up for newsletter</h5>
    <p>Excepteur sint occaecat cupidatat non proident, sunt in culpa qui officia deserunt</p>
    <div class="field">Enter Name</div>
    <div class="sub-row"><div class="field">Enter Email</div><div class="btn-sub">SUBSCRIBE</div></div>
  </div>
  <div class="foot-col" style="left:987px">
    <h5>Quick Links</h5>
    <ul class="links"><li>Home</li><li>Philosophy</li><li>Performance</li><li>Team</li><li>Commentary</li><li>Contact</li></ul>
  </div>
</footer>

<div class="wrap copyright">© Copyright Ashford Lane Investment 2017. All rights reserved</div>

</body>
</html>
```